Conflict prevention NGO needs business cards ASAP

We are a small NGO based in New Caledonia working on conflict prevention, and will be attending a WCA-sponsored conference on small arms next month. Our work involves campaigning against the proliferation of small arms in this post-conflict South Pacific island, and we need business cards to match that purpose.
Our three basic guidelines are the following:
1. We would like the logo of our organisation (see attached) included on this card. We are open to a redesign of this logo to something more stylised or abstract.
2. The card would need to be double-sided: one side in French, the other in English. The text should ideally be minimalist, uncluttered, clear and concise. We prefer the card to visually communicate our mission. As such, we would like the card to present a central image or logo, which would give us the option of printing a texture onto that image/logo later.
3. I have attached images which might inspire the designer (bullets and the famous knotted gun statue). However, these are NOT prescriptive; they are simply thematic ideas, and designers should use their own creative license. We only ask that the overall business card communicate professionalism and a seriousness of purpose, rather than sentimentalism or idealism.
Thanks to everyone who is willing to offer up a design idea! I am grateful for your time, and look forward to viewing your ideas. I apologise, but this has to be a rush job. Please get in touch if you need further guidance.
Please note that our new website will go live on Wednesday evening (Brisbane time), in case it can provide inspiration: http://www.lagonclair.org/
Business
ENGLISH SIDE
[Name, Position] Tomas Verhalen, Director
[Organisation] The Centre for a Bright Lagoon
[Sub-Title] The first New Caledonian think tank
[Tel] +61497215304
[Email] centrelagonclair@mailvero.net
[Website] http://www.lagonclair.org/
FRENCH SIDE
[Name, Position] Tomas Verhalen, Directeur
[Organisation] Le Centre pour le Lagon Clair
[Sub-Title] Le premier pôle de réflexion calédonien
[Tel] +61497215304
*Note: We are flexible on the exact way you present the above information, and you may wish to use icons instead of "Tel." for example.

```html
<!DOCTYPE html>
<html lang="en">
<head>
<meta charset="utf-8">
<title>The Centre for a Bright Lagoon – Business Cards</title>
<link rel="stylesheet" href="https://fonts.googleapis.com/css2?family=Jost:wght@400;500&family=Roboto+Condensed:wght@400&display=swap">
<style>
  :root {
    --backdrop: #e9e7e3;
    --card-body: #232426;
    --card-body-edge: #1c1d1f;
    --band-top: #2b86c8;
    --band-bottom: #1f4f99;
    --brand-blue: #2a86cf;
    --mark-blue: #1f6fb8;
    --mark-frame: #3a8fd6;
    --text-light: #f2f2f2;
    --icon-phone: #d8392b;
    --icon-mail: #e8d43a;
    --icon-web: #3aa84a;
  }
  * { box-sizing: border-box; margin: 0; padding: 0; }
  html, body { width: 1200px; height: 800px; overflow: hidden; }
  body {
    background: var(--backdrop);
    position: relative;
    font-family: "Roboto Condensed", "Arial Narrow", sans-serif;
  }
  .card-stack {
    position: absolute;
    left: 344px;
    top: 94px;
    display: flex;
    flex-direction: column;
    gap: 16px;
  }
  .business-card {
    position: relative;
    width: 512px;
    height: 298px;
    background: linear-gradient(160deg, var(--card-body) 0%, var(--card-body-edge) 100%);
    box-shadow: 0 6px 14px rgba(0,0,0,0.25);
    overflow: hidden;
  }
  .side-band {
    position: absolute;
    left: 0; top: 0; bottom: 0;
    width: 30px;
    background: linear-gradient(180deg, var(--band-top), var(--band-bottom));
  }
  .brand-mark {
    position: absolute;
    left: 47px;
    top: 37px;
    width: 82px;
    height: 82px;
    background: var(--mark-blue);
    border: 4px solid var(--mark-frame);
  }
  .brand-lockup {
    position: absolute;
    left: 145px;
    top: 61px;
    font-family: "Jost", "Futura", sans-serif;
  }
  .org-name {
    color: var(--brand-blue);
    font-size: 16px;
    font-weight: 400;
    letter-spacing: 0.6px;
    text-transform: uppercase;
    white-space: nowrap;
  }
  .org-tagline {
    color: var(--text-light);
    font-size: 11.5px;
    font-weight: 500;
    letter-spacing: 1.6px;
    margin-top: 4px;
    white-space: nowrap;
  }
  .person {
    position: absolute;
    left: 50px;
    top: 156px;
  }
  .person-name {
    color: var(--brand-blue);
    font-size: 21px;
    letter-spacing: 0.8px;
    text-transform: uppercase;
  }
  .person-role {
    color: var(--text-light);
    font-size: 15px;
    margin-top: 2px;
  }
  .contact-list {
    position: absolute;
    left: 50px;
    top: 221px;
    list-style: none;
  }
  .contact-item {
    display: flex;
    align-items: center;
    gap: 6px;
    height: 20px;
    color: var(--text-light);
    font-size: 13.5px;
  }
  .contact-icon { width: 13px; height: 13px; flex: none; }
</style>
</head>
<body>
  <main class="card-stack">
    <section class="business-card" lang="en">
      <div class="side-band"></div>
      <div class="brand-mark"></div>
      <div class="brand-lockup">
        <h1 class="org-name">The Centre for a Bright Lagoon</h1>
        <p class="org-tagline">The First New Caledonian Think Tank</p>
      </div>
      <div class="person">
        <h2 class="person-name">Tomas Verhalen</h2>
        <p class="person-role">Director</p>
      </div>
      <ul class="contact-list">
        <li class="contact-item">
          <svg class="contact-icon" viewBox="0 0 16 16"><path fill="var(--icon-phone)" d="M3.5 1.5l2.5 0 1.2 3.2-1.6 1.2a8 8 0 0 0 4.5 4.5l1.2-1.6 3.2 1.2v2.5c0 .8-.7 1.5-1.5 1.5A12.5 12.5 0 0 1 2 3c0-.8.7-1.5 1.5-1.5z"/></svg>
          <span>+61497215304</span>
        </li>
        <li class="contact-item">
          <svg class="contact-icon" viewBox="0 0 16 16"><rect x="1" y="3" width="14" height="10" fill="var(--icon-mail)"/><path d="M1 3l7 6 7-6" fill="none" stroke="#232426" stroke-width="1.2"/></svg>
          <span>centrelagonclair@mailvero.net</span>
        </li>
        <li class="contact-item">
          <svg class="contact-icon" viewBox="0 0 16 16"><circle cx="8" cy="8" r="7" fill="var(--icon-web)"/><path d="M1 8h14M8 1c-3 3-3 11 0 14M8 1c3 3 3 11 0 14" fill="none" stroke="#232426" stroke-width="1"/></svg>
          <span>www.lagonclair.org</span>
        </li>
      </ul>
    </section>

    <section class="business-card" lang="fr">
      <div class="side-band"></div>
      <div class="brand-mark"></div>
      <div class="brand-lockup">
        <h1 class="org-name">Le Centre pour le Lagon Clair</h1>
        <p class="org-tagline">Le premier pôle de réflexion calédonien</p>
      </div>
      <div class="person">
        <h2 class="person-name">Tomas Verhalen</h2>
        <p class="person-role">Directeur</p>
      </div>
      <ul class="contact-list">
        <li class="contact-item">
          <svg class="contact-icon" viewBox="0 0 16 16"><path fill="var(--icon-phone)" d="M3.5 1.5l2.5 0 1.2 3.2-1.6 1.2a8 8 0 0 0 4.5 4.5l1.2-1.6 3.2 1.2v2.5c0 .8-.7 1.5-1.5 1.5A12.5 12.5 0 0 1 2 3c0-.8.7-1.5 1.5-1.5z"/></svg>
          <span>+61497215304</span>
        </li>
        <li class="contact-item">
          <svg class="contact-icon" viewBox="0 0 16 16"><rect x="1" y="3" width="14" height="10" fill="var(--icon-mail)"/><path d="M1 3l7 6 7-6" fill="none" stroke="#232426" stroke-width="1.2"/></svg>
          <span>centrelagonclair@mailvero.net</span>
        </li>
        <li class="contact-item">
          <svg class="contact-icon" viewBox="0 0 16 16"><circle cx="8" cy="8" r="7" fill="var(--icon-web)"/><path d="M1 8h14M8 1c-3 3-3 11 0 14M8 1c3 3 3 11 0 14" fill="none" stroke="#232426" stroke-width="1"/></svg>
          <span>www.lagonclair.org</span>
        </li>
      </ul>
    </section>
  </main>
</body>
</html>
```